Halvercott Orthodontics business card

Using our existing logo (created with ArtFolio), please create a tasteful, contemporary business card. We are father and daughter orthodontists specializing in braces, clarafit, etc to design healthy, beautiful smiles for children, adolescents, and adults. We would like the design to be family-friendly but not childish.
The final design should include all of the information without looking cluttered (I hope! If necessary to achieve an optimal design, please consider making the card double-sided)
Purple, black, silver on a white card
Please include the following information:
Halvercott Orthodontics (logo)
Marguerite L. Halvercott, DMD
Douglas R. Halvercott, DMD

312 Bramblewood Street
North Andover, MA 01899
978.555.0142

847C Quarry Hollow Street
Methuen, MA 01898
978.555.0187

email frontdesk@halvercottortho.example
website www.halvercottortho.example

```html
<!DOCTYPE html>
<html lang="en">
<head>
<meta charset="utf-8">
<title>Halvercott Orthodontics business card</title>
<link href="https://fonts.googleapis.com/css2?family=Montserrat:wght@400;500;600&display=swap" rel="stylesheet">
<style>
  :root {
    --page-bg: #ebebeb;
    --card-white: #ffffff;
    --purple: #642d96;
    --purple-light: #7b48b3;
    --ink-on-purple: #ffffff;
  }
  * { margin: 0; padding: 0; box-sizing: border-box; }
  html, body {
    width: 1200px; height: 1164px; overflow: hidden;
    background: var(--page-bg);
    font-family: "Montserrat", Arial, sans-serif;
  }
  .card-set {
    position: absolute; left: 40px; top: 420px;
    display: flex; gap: 40px;
  }
  .card {
    position: relative; width: 540px; height: 324px;
    background: var(--card-white);
    box-shadow: 0 1px 3px rgba(0,0,0,0.12);
    overflow: hidden;
  }
  .wordmark {
    color: var(--purple); font-weight: 500;
    display: flex; align-items: center; gap: 10px;
    white-space: nowrap;
  }
  .wordmark-dot {
    width: 14px; height: 14px; border-radius: 50%;
    background: var(--purple);
  }
  .card-front .wordmark {
    position: absolute; left: 0; right: 0; top: 0; bottom: 0;
    justify-content: center; font-size: 26px; letter-spacing: 0.5px;
  }
  .back-shape { position: absolute; inset: 0; }
  .card-back .wordmark {
    position: absolute; left: 22px; top: 150px; font-size: 15px;
  }
  .card-back .wordmark-dot { width: 10px; height: 10px; }
  .contact {
    position: absolute; right: 34px; top: 40px;
    text-align: right; color: var(--ink-on-purple);
  }
  .doctor-names { font-weight: 600; font-size: 16px; line-height: 21px; }
  .office { margin-top: 50px; font-size: 12px; line-height: 18px; }
  .office + .office { margin-top: 13px; }
  .web { margin-top: 9px; font-size: 12px; line-height: 18px; }
</style>
</head>
<body>
  <main class="card-set">
    <section class="card card-front">
      <div class="wordmark"><span class="wordmark-dot"></span>Halvercott Orthodontics</div>
    </section>

    <section class="card card-back">
      <svg class="back-shape" width="540" height="324" viewBox="0 0 540 324" aria-hidden="true">
        <rect width="540" height="324" fill="var(--purple)"/>
        <path d="M0,20 C10,44 50,48 120,48 C205,48 268,58 276,140 C283,222 250,290 200,324 L0,324 Z" fill="var(--purple-light)"/>
        <path d="M0,26 C10,50 50,54 120,54 C200,54 257,64 265,140 C272,220 240,290 190,324 L0,324 Z" fill="var(--card-white)"/>
      </svg>
      <div class="wordmark"><span class="wordmark-dot"></span>Halvercott Orthodontics</div>
      <div class="contact">
        <p class="doctor-names">Marguerite L. Halvercott, DMD<br>Douglas R. Halvercott, DMD</p>
        <p class="office">847C Quarry Hollow Street<br>Methuen, MA 01898<br>978.555.0187</p>
        <p class="office">312 Bramblewood Street<br>North Andover, MA 01899<br>978.555.0142</p>
        <p class="web">frontdesk@halvercottortho.example<br>www.halvercottortho.example</p>
      </div>
    </section>
  </main>
</body>
</html>
```